Helicopter company requires newspaper ad

"Ridgeline Aviators" is an agricultural helicopter company based in Victoria, Australia. We need an advert design for use in newspapers and also possibly social media. Our company specialises in using a helicopter for various agricultural work such as Spraying weeds ("Cropdusting"), spreading fertiliser. This advert will be targeted at farmers in our service area, Our customers are mainly dairy and cow farmers and our services are aimed at increasing their farm productivity. The final design should inform potential and existing customers about our services and the benefits of them. I will attach files of our logo and some existing advertising material for guidance. We would like the ad to feature the blue and green colours in our logo Please feel free to view our website and facebook page to see more about what we do. www.ridgelineaviators.com.au Some text we would like included Spraying: -Accurate -Time Efficient -Zero crop damage -Cost efficient Fertiliser Spreading: -Accurate, Pattern-tested equipment -Zero crop damage or wheel marks -Ability to load product out of a truck, bin or bulk bags -Cost effective, Prices from $32 per hectare depending on spread rate The final advert size should be 195 mm wide x 186 mm high Thanks :)

Target Market(s)

Farmers, Agriculture Industry

Industry/Entity Type

Agribusiness

Colors

Designer to choose colors to be used in the design.

Requirements
Must have
• Phone number 0491 635 087
• The text included in the decription, or variations of this

```html
<!DOCTYPE html>
<html lang="en">
<head>
<meta charset="utf-8">
<title>Ridgeline Aviators – Summer Crops Advert</title>
<link href="https://fonts.googleapis.com/css2?family=Oswald:wght@700&family=Open+Sans:wght@400;700&display=swap" rel="stylesheet">
<style>
  :root {
    --brand-blue: #1e76bf;
    --brand-green: #7cc242;
    --band-green: #76b82a;
    --navy: #023a6e;
    --white: #ffffff;
    --ink: #111111;
    --sky-top: #8fd3f8;
    --sky-low: #d9eef8;
    --field: #8fb14f;
  }
  * { margin: 0; padding: 0; box-sizing: border-box; }
  html, body { width: 1200px; height: 1145px; overflow: hidden; background: var(--brand-blue); }
  .advert {
    position: relative;
    width: 1200px;
    height: 1145px;
    background: var(--brand-blue);
    font-family: "Open Sans", Arial, sans-serif;
    color: var(--white);
    overflow: hidden;
  }
  .hero { position: absolute; left: 0; top: 0; width: 1200px; height: 560px; }
  .brand-badge {
    position: absolute;
    left: 49px; top: 299px;
    width: 292px; height: 244px;
    border-radius: 50%;
    background: var(--white);
    border: 15px solid var(--brand-blue);
    display: flex; align-items: center; justify-content: center;
    transform: rotate(8deg);
  }
  .brand-name {
    font-family: "Open Sans", Arial, sans-serif;
    font-weight: 700;
    font-size: 30px;
    line-height: 1.1;
    color: var(--brand-blue);
    text-align: center;
    transform: rotate(-8deg);
  }
  .headline {
    position: absolute;
    left: 0; right: 0; top: 588px;
    text-align: center;
    font-family: "Oswald", Impact, sans-serif;
    font-weight: 700;
    font-size: 52px;
    line-height: 1;
    letter-spacing: -0.5px;
    text-transform: uppercase;
  }
  .spreading-card {
    position: absolute;
    left: 79px; top: 690px;
    width: 459px; height: 370px;
    background: var(--white);
    border-radius: 6px 6px 0 0;
    color: var(--ink);
    padding: 28px 30px 0 32px;
  }
  .section-title {
    font-family: "Oswald", Impact, sans-serif;
    font-weight: 700;
    font-size: 34px;
    line-height: 1;
    text-transform: uppercase;
  }
  .spreading-card .section-title { color: var(--brand-blue); }
  .feature-list { list-style: none; margin-top: 30px; }
  .feature-list li {
    position: relative;
    padding-left: 27px;
    font-size: 21px;
    line-height: 26px;
    margin-bottom: 9px;
  }
  .feature-list li::before {
    content: "";
    position: absolute; left: 2px; top: 12px;
    width: 7px; height: 7px; border-radius: 50%;
    background: var(--ink);
  }
  .feature-list li.wrap { margin-top: 10px; margin-bottom: 18px; }
  .spraying { position: absolute; left: 580px; top: 690px; width: 540px; }
  .spraying .section-title { margin-left: 39px; }
  .benefit {
    position: absolute;
    width: 260px;
    text-align: center;
    font-weight: 700;
    font-size: 23px;
  }
  .benefit svg { display: block; margin: 0 auto 20px; }
  .benefit-accurate { left: -23px; top: 60px; }
  .benefit-time { left: 255px; top: 60px; }
  .benefit-crop { left: -23px; top: 212px; }
  .benefit-cost { left: 255px; top: 212px; }
  .contact-bar { position: absolute; left: 0; top: 1055px; width: 1200px; height: 90px; }
  .phone {
    position: absolute; left: 79px; top: 1070px;
    display: flex; align-items: center; gap: 28px;
  }
  .phone-icon {
    width: 62px; height: 62px; border-radius: 50%;
    background: var(--white);
    display: flex; align-items: center; justify-content: center;
  }
  .phone-number {
    font-family: "Oswald", Impact, sans-serif;
    font-weight: 700;
    font-size: 62px;
    line-height: 1;
    letter-spacing: -1px;
  }
  .website {
    position: absolute; left: 634px; top: 1092px;
    display: flex; align-items: center; gap: 18px;
    font-weight: 700; font-size: 23px;
  }
</style>
</head>
<body>
<div class="advert">

  <svg class="hero" viewBox="0 0 1200 560" aria-hidden="false">
    <defs>
      <linearGradient id="sceneTone" x1="0" y1="0" x2="0" y2="1">
        <stop offset="0" stop-color="var(--sky-top)"/>
        <stop offset="0.45" stop-color="var(--sky-low)"/>
        <stop offset="0.6" stop-color="var(--field)"/>
        <stop offset="1" stop-color="#9fbf6a"/>
      </linearGradient>
    </defs>
    <path d="M0 0 H1200 V248 C1010 420 720 540 320 540 L0 380 Z" fill="var(--white)"/>
    <path d="M0 0 H1200 V218 C1000 400 700 515 330 515 L0 370 Z" fill="var(--brand-green)"/>
    <path role="img" aria-label="Photo: helicopter with a spray boom spraying a green paddock under a blue sky with rolling hills"
          d="M0 0 H1176 C1150 200 930 470 330 492 L0 364 Z" fill="url(#sceneTone)"/>
  </svg>

  <div class="brand-badge">
    <span class="brand-name">Ridgeline<br>Aviators</span>
  </div>

  <h1 class="headline">Summer crops need spraying or fertiliser?</h1>

  <section class="spreading-card">
    <h2 class="section-title">Spreading</h2>
    <ul class="feature-list">
      <li>Accurate, Pattern-tested equipment</li>
      <li>Zero crop damage or wheel marks</li>
      <li class="wrap">Ability to load out of a Truck, Bin or bulk-bags</li>
      <li>Competitive Prices (from $32 per hectare depending on spread rate)</li>
    </ul>
  </section>

  <section class="spraying">
    <h2 class="section-title">Spraying</h2>

    <div class="benefit benefit-accurate">
      <svg width="74" height="74" viewBox="0 0 74 74" fill="none" stroke="#fff" stroke-width="3" stroke-linejoin="round">
        <path d="M8 14 H58 A4 4 0 0 1 62 18 V66 H10 A4 4 0 0 1 6 62 V16"/>
        <path d="M4 38 L34 70 L44 60 L14 28 Z"/>
        <path d="M14 38 l4 -4 M20 44 l4 -4 M26 50 l4 -4 M32 56 l4 -4"/>
        <path d="M34 36 L62 8 L68 14 L40 42 L32 44 Z"/>
        <path d="M50 58 h2 M56 58 h2"/>
      </svg>
      Accurate
    </div>

    <div class="benefit benefit-time">
      <svg width="74" height="74" viewBox="0 0 74 74" fill="none" stroke="#fff" stroke-width="3">
        <circle cx="30" cy="32" r="26"/>
        <circle cx="30" cy="32" r="20"/>
        <path d="M30 16 V32 L40 38"/>
        <circle cx="50" cy="50" r="14"/>
        <circle cx="50" cy="50" r="5"/>
        <path d="M50 32 v6 M50 62 v6 M32 50 h6 M62 50 h6"/>
      </svg>
      Time Efficient
    </div>

    <div class="benefit benefit-crop">
      <svg width="80" height="82" viewBox="0 0 80 82" fill="none" stroke="#fff" stroke-width="3" stroke-linecap="round">
        <circle cx="40" cy="18" r="8"/>
        <path d="M40 2 v4 M40 30 v4 M24 18 h4 M52 18 h4 M29 7 l3 3 M51 7 l-3 3 M29 29 l3 -3 M51 29 l-3 -3"/>
        <path d="M2 80 H78"/>
        <path d="M40 80 V50 M40 58 C32 50 30 46 40 44 C50 46 48 50 40 58"/>
        <path d="M14 80 V66 M14 70 C6 64 6 60 14 62 M14 70 C22 64 22 60 14 62"/>
        <path d="M66 80 V66 M66 70 C58 64 58 60 66 62 M66 70 C74 64 74 60 66 62"/>
      </svg>
      Zero Crop Damage
    </div>

    <div class="benefit benefit-cost">
      <svg width="74" height="74" viewBox="0 0 74 74" fill="none" stroke="#fff" stroke-width="3" stroke-linejoin="round">
        <path d="M30 4 H50 L44 14 C58 20 62 34 58 46 H22 C18 34 22 20 36 14 Z"/>
        <path d="M44 24 C36 22 32 28 40 31 C48 34 44 40 36 38 M40 20 v22"/>
        <path d="M2 52 C10 46 20 48 28 52 H44 A4 4 0 0 1 44 60 H30 M2 60 L18 70 H56 V50 H66 V70 H56"/>
      </svg>
      Cost-Effective
    </div>
  </section>

  <svg class="contact-bar" viewBox="0 0 1200 90" aria-hidden="true">
    <rect x="0" y="23" width="1200" height="67" fill="var(--navy)"/>
    <polygon points="0,0 573,0 598,90 0,90" fill="var(--band-green)"/>
  </svg>

  <div class="phone">
    <div class="phone-icon">
      <svg width="36" height="36" viewBox="0 0 24 24" fill="var(--band-green)">
        <path d="M6.6 10.8a15.1 15.1 0 0 0 6.6 6.6l2.2-2.2a1 1 0 0 1 1-.25 11.4 11.4 0 0 0 3.6.6 1 1 0 0 1 1 1V20a1 1 0 0 1-1 1A17 17 0 0 1 3 4a1 1 0 0 1 1-1h3.5a1 1 0 0 1 1 1c0 1.25.2 2.45.6 3.6a1 1 0 0 1-.25 1z"/>
      </svg>
    </div>
    <span class="phone-number">0491 635 087</span>
  </div>

  <div class="website">
    <svg width="36" height="36" viewBox="0 0 36 36" fill="none" stroke="#fff" stroke-width="2.5">
      <circle cx="18" cy="18" r="16"/>
      <ellipse cx="18" cy="18" rx="7" ry="16"/>
      <path d="M2 18 H34 M5 10 H31 M5 26 H31"/>
    </svg>
    <span>www.ridgelineaviators.com.au</span>
  </div>

</div>
</body>
</html>
```